Halvern Aviation Group - "Coming Soon" Main Company Webpage

Design a main webpage that can be posted while a fully functional website is constructed. The design should be created to convey a sense of luxury and exclusivity. The main page should contain only one photo as the background. The photo I believe to show "luxury" and "Exclusivity" is listed as "Global Luxury Photo". I have included two other photos as well to aid in providing a variety of presentations.
The "Member PQTR" logo should appear somewhere on the main page but be less prevalent than the main company logo. "Coming Soon" should also appear to convey that a website is being constructed.
Tabs for the website:
- Aircraft Management
- Aircraft Sales
- Pilot Services
- Charter
- Flight Training

```html
<!DOCTYPE html>
<html lang="en">
<head>
<meta charset="UTF-8">
<title>Halvern Aviation Group — Coming Soon</title>
<link href="https://fonts.googleapis.com/css2?family=Jost:wght@400;500;600&family=Playfair+Display:ital,wght@0,400;1,700&display=swap" rel="stylesheet">
<style>
  :root {
    --brand-blue: #0d5bab;
    --panel-blue: #1160b8;
    --navy: #14305e;
    --ink: #1b1b1b;
    --white: #ffffff;
    --divider: #e2e2e2;
    --badge-light: #d6dbe2;
    --badge-dark: #aab3c0;
    --sky-warm: #e8a58f;
    --sky-mid: #8593a8;
    --sky-deep: #2c5189;
  }
  * { margin: 0; padding: 0; box-sizing: border-box; }
  html, body { width: 1200px; height: 610px; overflow: hidden; }
  body { position: relative; font-family: "Jost", sans-serif; background: var(--white); }

  .top-bar {
    position: absolute; left: 0; top: 0; width: 1200px; height: 26px;
    background: var(--brand-blue); color: var(--white);
    font-size: 11px; letter-spacing: 0.6px;
    display: flex; justify-content: flex-end; align-items: center; padding-right: 113px;
  }
  .top-bar span { margin-left: 14px; }

  .site-header {
    position: absolute; left: 0; top: 26px; width: 1200px; height: 61px; background: var(--white);
  }
  .brand {
    position: absolute; left: 113px; top: 10px; color: var(--navy);
    font-weight: 600; text-transform: uppercase; line-height: 1;
    display: flex; align-items: center; gap: 9px;
  }
  .brand-mark { width: 13px; height: 13px; background: var(--brand-blue); }
  .brand-name { font-size: 27px; letter-spacing: 3px; }
  .brand-name small { display: block; font-size: 11px; letter-spacing: 2.4px; margin-top: 4px; }

  .main-nav {
    position: absolute; left: 475px; top: 0; height: 61px; display: flex;
    border-left: 1px solid var(--divider);
  }
  .main-nav a {
    display: flex; align-items: center; height: 61px; padding: 0 12.5px;
    color: var(--ink); text-decoration: none; font-size: 12.8px; text-transform: uppercase;
    border-right: 1px solid var(--divider);
  }

  .hero {
    position: absolute; left: 0; top: 87px; width: 1200px; height: 523px;
    background:
      radial-gradient(ellipse 260px 120px at 620px 90px, rgba(240,175,155,0.75), transparent 70%),
      radial-gradient(ellipse 200px 90px at 380px 60px, rgba(225,170,160,0.55), transparent 70%),
      radial-gradient(ellipse 240px 100px at 750px 230px, rgba(235,165,140,0.5), transparent 70%),
      radial-gradient(ellipse 220px 80px at 150px 220px, rgba(200,175,175,0.45), transparent 70%),
      radial-gradient(ellipse 320px 150px at 960px 330px, rgba(210,220,235,0.55), transparent 70%),
      radial-gradient(ellipse 300px 90px at 500px 420px, rgba(120,150,190,0.5), transparent 70%),
      radial-gradient(ellipse 260px 80px at 150px 470px, rgba(90,125,175,0.55), transparent 70%),
      linear-gradient(180deg, #8f8c93 0%, #a09097 22%, #8a8a9c 40%, #6a7f9e 58%, #44679a 78%, var(--sky-deep) 100%);
  }

  .intro-panel {
    position: absolute; left: 113px; top: 282px; width: 428px; height: 171px;
    background: var(--panel-blue); color: var(--white);
  }
  .corner { position: absolute; width: 27px; height: 27px; }
  .corner-tr { left: 521px; top: 276px; border-top: 5px solid var(--white); border-right: 5px solid var(--white); }
  .corner-bl { left: 106px; top: 433px; border-bottom: 5px solid var(--white); border-left: 5px solid var(--white); }

  .eyebrow-line { position: absolute; left: 100px; top: 320px; width: 35px; height: 1px; background: var(--white); }
  .eyebrow {
    position: absolute; left: 133px; top: 312px; width: 75px; height: 18px;
    background: #111; color: var(--white); font-size: 12.5px;
    display: flex; align-items: center; justify-content: center; letter-spacing: 0.4px;
  }
  .headline {
    position: absolute; left: 129px; top: 321px; color: var(--white);
    font-family: "Playfair Display", serif; font-size: 63px; font-weight: 400; line-height: 1;
  }
  .headline em { font-weight: 700; font-style: italic; }
  .subline {
    position: absolute; left: 132px; top: 406px; color: var(--white); font-size: 20px; font-weight: 400;
  }

  .slider-controls {
    position: absolute; left: 11px; top: 559px; width: 79px; height: 40px;
    border: 1px solid rgba(255,255,255,0.85); display: flex;
  }
  .slider-controls button {
    flex: 1; background: transparent; border: 0; display: flex; align-items: center; justify-content: center;
  }
  .slider-controls button + button { border-left: 1px solid rgba(255,255,255,0.85); }

  .member-badge {
    position: absolute; left: 1029px; top: 556px; width: 108px; height: 38px;
    background: linear-gradient(180deg, var(--badge-light), var(--badge-dark));
    border-radius: 9px; border: 1px solid rgba(255,255,255,0.7);
    box-shadow: 0 2px 6px rgba(0,0,0,0.25);
  }

  .social-rail-line { position: absolute; left: 1172px; top: 487px; width: 1px; height: 38px; background: rgba(255,255,255,0.7); }
  .social-links { position: absolute; left: 1161px; top: 529px; display: flex; flex-direction: column; gap: 3px; }
  .social-links a {
    display: flex; align-items: center; justify-content: center;
    width: 20px; height: 20px; border: 1px solid rgba(255,255,255,0.85);
  }
  .social-links a::after {
    content: ""; width: 7px; height: 7px; background: var(--white);
  }
</style>
</head>
<body>
  <div class="top-bar">
    <span>PHONE : 555-014-2290</span><span>|</span>
    <span>EMAIL: HELLO@HALVERNAVIATION.EXAMPLE</span><span>|</span>
    <span>ABOUT</span><span>|</span><span>CONTACT</span>
  </div>

  <header class="site-header">
    <div class="brand">
      <span class="brand-mark"></span>
      <span class="brand-name">Halvern<small>Aviation Group</small></span>
    </div>
    <nav class="main-nav">
      <a href="#">Aircraft Management</a>
      <a href="#">Aircraft Sales</a>
      <a href="#">Pilot Services</a>
      <a href="#">Charter</a>
      <a href="#">Flight Training</a>
    </nav>
  </header>

  <section class="hero" role="img" aria-label="Private business jet flying above pink sunset clouds"></section>

  <div class="intro-panel"></div>
  <div class="corner corner-tr"></div>
  <div class="corner corner-bl"></div>
  <div class="eyebrow-line"></div>
  <div class="eyebrow">WE ARE</div>
  <h1 class="headline">Coming <em>Soon</em></h1>
  <p class="subline">Our Website is Under construction</p>

  <div class="slider-controls">
    <button aria-label="Previous slide"><svg width="10" height="14" viewBox="0 0 10 14"><path d="M8 1 2 7l6 6" fill="none" stroke="#fff" stroke-width="1.8"/></svg></button>
    <button aria-label="Next slide"><svg width="10" height="14" viewBox="0 0 10 14"><path d="M2 1l6 6-6 6" fill="none" stroke="#fff" stroke-width="1.8"/></svg></button>
  </div>

  <div class="member-badge" role="img" aria-label="Member PQTR badge"></div>

  <div class="social-rail-line"></div>
  <div class="social-links">
    <a href="#" aria-label="Social profile"></a>
    <a href="#" aria-label="Video channel"></a>
    <a href="#" aria-label="Professional network"></a>
  </div>
</body>
</html>
```